Business card design needed

I am a local business in the Blue Mountains area of Sydney. I am a sole trader and the business has been operating 7 months. To date the business has been built on referrals only and all my clinets for both home & commercial services are themselves business owners. I specialise in Home and Office cleaning and small business cleaning for example cafes, restuarants, health clinics.
I would like a clean looking design( maybe a white background). If its possible(not madatory) to incorporate a duster, or mop & bucket into the design or roof tops to communicate business premises that would be great. I would like my clients to know what the business is from the card. My uniform is navy with red/pink logo on .Attatched is the unifrom logo but it is not critical to match the font for the business card.
please put my name on contact details; Carol Whitby, Business owner.
Updates
Thank you very much to all the designers and their work efforts to submit a design for Bright Feather Domestic Services. I have made a decision to accept the deign that Velo Design of the United States submitted. Again Many thanks. Carol
Target Market(s)
business owners, generally women between 35-55
Industry/Entity Type
Small Business
Contact Information for Business Card
Bright Feather Domestic Services,
specialist in Home & Small business cleaning
Ferndale Ridge NSW
tel: 0491570156 0491tidyup
Logo Text
Bright Feather Domestic Servies
Logo styles of interest
Emblem Logo
Abstract Logo
Wordmark Logo
Look and feel

```html
<!DOCTYPE html>
<html lang="en">
<head>
<meta charset="utf-8">
<title>Bright Feather Domestic Services – Business Card</title>
<link rel="stylesheet" href="https://fonts.googleapis.com/css2?family=Alegreya+Sans:wght@500;700&display=swap">
<style>
  :root {
    --paper: #ffffff;
    --ink: #1c1c1c;
    --rule: #1a1a1a;
    --rule-mid: #a9adad;
  }
  html, body {
    margin: 0;
    padding: 0;
    width: 1200px;
    height: 1000px;
    overflow: hidden;
    background: var(--paper);
  }
  .card {
    position: relative;
    width: 1200px;
    height: 1000px;
    font-family: "Alegreya Sans", "Candara", sans-serif;
    color: var(--ink);
  }
  .rule-h {
    position: absolute;
    left: 148px;
    width: 902px;
    height: 4px;
    background: var(--rule);
  }
  .rule-h.top { top: 232px; }
  .rule-h.bottom { top: 764px; }
  .rule-v {
    position: absolute;
    top: 272px;
    width: 4px;
    height: 453px;
    background: linear-gradient(to bottom, var(--rule) 0%, var(--rule-mid) 50%, var(--rule) 100%);
  }
  .rule-v.left { left: 106px; }
  .rule-v.right { left: 1087px; }

  .brand {
    margin: 0;
    font-weight: 700;
    color: var(--ink);
  }
  .brand-name {
    position: absolute;
    left: 233px;
    top: 374px;
    font-size: 93px;
    line-height: 1;
    letter-spacing: 1px;
    white-space: nowrap;
  }
  .brand-line {
    position: absolute;
    left: 468px;
    top: 476px;
    font-size: 66px;
    line-height: 1;
    white-space: nowrap;
  }

  .contact {
    position: absolute;
    left: 160px;
    top: 562px;
    margin: 0;
    padding: 0;
    list-style: none;
    font-size: 29px;
    font-weight: 700;
    line-height: 33px;
    white-space: nowrap;
  }
  .contact li::before {
    content: "•";
    margin-right: 6px;
    font-size: 24px;
  }
  .tagline {
    position: absolute;
    left: 0;
    width: 1200px;
    top: 692px;
    margin: 0;
    text-align: center;
    font-size: 40px;
    font-weight: 700;
    line-height: 46px;
    white-space: nowrap;
  }
</style>
</head>
<body>
  <div class="card">
    <div class="rule-h top"></div>
    <div class="rule-v left"></div>
    <div class="rule-v right"></div>

    <h1 class="brand">
      <span class="brand-name">BRIGHT FEATHER</span>
      <span class="brand-line">Domestic Services</span>
    </h1>

    <ul class="contact">
      <li>Carol Whitby, Business owner</li>
      <li>Ferndale Ridge NSW</li>
      <li>tel: 049 157 0156</li>
    </ul>

    <p class="tagline">• specialist in home &amp; small business cleaning •</p>

    <div class="rule-h bottom"></div>
  </div>
</body>
</html>
```